Manufacturer's Representative Group needs a clean new Website

We represent and sell a number of suppliers that design and build products used in Biopharmaceutical manufacturing. Our sales region is in the central US. Our customer base is scientific / engineering based - so clean, we organized design with a focus on the products - easy and clear navigation is necessary. We do not sell direct or warehouse product - so e-commerce is not needed. Our customers will use the website for reference on what we do and offer - we will use the site as a platform to present products from each vendor and the home page will be used to capture an overview and draw users deeper into the site. You can view our current site - which needs A LOT of help to get ideas on products represented and types of products

Target Market(s)

Engineers and Pharmaceutical / Bio pharm end users

Industry/Entity Type

E-Commerce

Number of Pages Required

2 page

Font styles to use
Sans Serif

Requirements
Must have
• I need a home page that provides a snapshot of my company and the product lines we represent - then a second page that I can copy as a template for each line I rep as well as for an "About us / contact" page.
• I would like to be able to manage content on the pages so something easy to adjust pictures or add content is a must
• Must use our logo

```html
<!DOCTYPE html>
<html lang="en">
<head>
<meta charset="utf-8">
<title>Prairie Bio — Home</title>
<link href="https://fonts.googleapis.com/css2?family=Roboto:wght@400;500;700&display=swap" rel="stylesheet">
<style>
:root{
  --navy:#27235f;
  --orange:#f26129;
  --white:#ffffff;
  --text:#222222;
  --footer-bg:#f1f1f1;
  --field:#c9c9c9;
  --line:#e2e2e2;
}
*{margin:0;padding:0;box-sizing:border-box}
html,body{width:783px;height:1200px;overflow:hidden;background:var(--white)}
body{font-family:"Roboto",Arial,sans-serif;color:var(--text)}
.page{position:relative;width:783px;height:1200px;overflow:hidden}
.abs{position:absolute}

/* header */
.header{left:0;top:0;width:783px;height:68px;background:linear-gradient(90deg,#eef1f6,#f7f8fb 50%,#e9edf4)}
.brand{display:flex;align-items:center;gap:6px;font-size:19px;font-weight:400;color:var(--navy);white-space:nowrap}
.brand-dot{width:14px;height:14px;border-radius:50%;background:var(--orange)}
.header .brand{left:81px;top:24px}
.helpline{left:477px;top:20px;width:225px;height:33px;background:var(--white);border:1px solid #d6d6d6;border-radius:2px}
.helpline-photo{left:10px;top:0;width:24px;height:32px;background:linear-gradient(#c79b7d,#5a4a44)}
.helpline-text{left:43px;top:6px;font-size:8.3px;line-height:10.5px;color:var(--navy)}
.helpline-text em{font-style:normal;color:var(--orange)}

/* nav */
.nav{left:0;top:68px;width:783px;height:40px;background:rgba(39,35,95,.92)}
.nav-link{top:15px;font-size:8.6px;color:var(--white);text-transform:uppercase;letter-spacing:.1px}
.nav-link.active{color:var(--orange)}
.nav-social{top:13px;width:14px;height:14px;border-radius:50%;background:var(--white)}
.search{left:595px;top:12px;width:107px;height:17px;background:var(--white)}
.search svg{position:absolute;right:4px;top:3px}

/* hero */
.hero{left:0;top:108px;width:783px;height:241px;background:radial-gradient(ellipse at 60% 40%,#9cd4f0 0%,#3e7fc4 35%,#12357a 75%,#0a1f55 100%)}

/* about */
.about{left:0;top:349px;width:783px;height:143px;background:var(--orange)}
.section-title{font-size:16px;font-weight:500;white-space:nowrap}
.title-line{height:1px}
.about .section-title{left:81px;top:25px;color:var(--white)}
.about-text{left:81px;top:58px;width:515px;font-size:9.3px;line-height:11.7px;color:var(--white)}
.about-text b{font-weight:400;color:var(--navy)}
.btn-navy{left:612px;top:68px;width:90px;height:23px;background:var(--navy);color:var(--white);font-size:8.6px;display:flex;align-items:center;justify-content:center}

/* products */
.products .section-title{color:var(--navy)}
.accent{color:var(--orange)}
.card{top:565px;width:143px;height:178px;background:var(--navy);overflow:hidden}
.card-photo{left:0;top:0;width:143px;height:72px}
.card-title{left:0;top:82px;width:143px;text-align:center;font-size:12.5px;color:var(--white)}
.card-text{left:8px;top:102px;width:127px;text-align:center;font-size:7px;line-height:10.4px;color:var(--white)}
.card-btn{left:36px;top:145px;width:71px;height:15px;background:var(--orange);color:var(--white);font-size:6.8px;font-weight:700;display:flex;align-items:center;justify-content:center}
.card-hover{left:8px;top:9px;width:127px;height:159px;background:rgba(242,97,41,.82)}
.card-hover-title{left:0;top:14px;width:127px;text-align:center;font-size:17px;font-weight:400;line-height:19px;color:var(--white)}
.card-hover .card-title{left:-8px;top:73px;color:rgba(39,35,95,.35)}
.card-hover .card-text{left:0;top:93px;color:rgba(39,35,95,.3)}
.card-hover .card-btn{left:28px;top:136px;background:rgba(255,120,80,.5);color:rgba(255,255,255,.4)}
.hover-icon{top:80px;width:22px;height:22px;border-radius:50%;background:var(--white)}
.slider-arrow{top:633px;width:28px;height:28px;background:var(--navy);display:flex;align-items:center;justify-content:center}
.divider{left:0;top:760px;width:783px;height:1px;background:var(--line)}

/* companies */
.pager{top:778px;width:17px;height:16px;display:flex;align-items:center;justify-content:center}
.partner{top:820px;width:90px;height:50px;border:1px solid #9fb6cc;background:var(--white);display:flex;align-items:center;justify-content:center;font-size:10.5px;font-weight:500;color:var(--navy);text-align:center}

/* footer */
.footer{left:0;top:897px;width:783px;height:255px;background:var(--footer-bg)}
.footer .brand{left:81px;top:33px}
.footer-text{left:81px;top:70px;width:143px;font-size:7.8px;line-height:13px;text-align:justify;color:var(--text)}
.big-social{top:126px;width:33px;height:33px;border-radius:50%;background:#9a9a9a}
.big-social.primary{background:#3b5697}
.person-photo{top:32px;width:105px;height:103px;border:2px solid var(--navy)}
.contact-line{width:150px;text-align:center;font-size:10px;font-weight:500;color:var(--text)}
.mini-social{top:227px;width:16px;height:16px;border-radius:50%;background:#9a9a9a}
.mini-social.primary{background:#3b5697}
.field{left:559px;width:143px;background:var(--field);font-size:8.6px;color:var(--text);padding:8px 6px}
.btn-send{left:559px;top:204px;width:75px;height:25px;background:var(--navy);color:var(--white);font-size:8.6px;display:flex;align-items:center;justify-content:center}
.copyright{left:0;top:1152px;width:783px;height:48px;background:var(--navy);color:var(--white);font-size:7.5px;display:flex;align-items:center;justify-content:center}
</style>
</head>
<body>
<div class="page">

  <header class="header abs">
    <div class="brand abs"><span class="brand-dot"></span>Prairie Bio</div>
    <div class="helpline abs">
      <div class="helpline-photo abs" role="img" aria-label="Support agent with headset"></div>
      <p class="helpline-text abs">Need a helping hand? Call our office search<br>helpline for advice - <em>+1 5550134782</em></p>
    </div>
  </header>

  <nav class="nav abs">
    <span class="nav-link abs active" style="left:81px">Home</span>
    <span class="nav-link abs" style="left:128px">About Us</span>
    <span class="nav-link abs" style="left:192px">Our Products</span>
    <span class="nav-link abs" style="left:277px">Manufatur Link</span>
    <span class="nav-link abs" style="left:370px">Contact</span>
    <span class="nav-social abs" style="left:462px" aria-label="Social link"></span>
    <span class="nav-social abs" style="left:486px" aria-label="Social link"></span>
    <span class="nav-social abs" style="left:512px" aria-label="Social link"></span>
    <span class="nav-social abs" style="left:539px" aria-label="Social link"></span>
    <span class="nav-social abs" style="left:566px" aria-label="Social link"></span>
    <div class="search abs">
      <svg width="11" height="11" viewBox="0 0 11 11"><circle cx="4.5" cy="4.5" r="3.4" fill="none" stroke="#27235f" stroke-width="1.6"/><line x1="7" y1="7" x2="10" y2="10" stroke="#27235f" stroke-width="1.8"/></svg>
    </div>
  </nav>

  <div class="hero abs" role="img" aria-label="Close-up of glassy blue molecular structure"></div>

  <section class="about abs">
    <h2 class="section-title abs">About Us</h2>
    <svg class="abs" style="left:81px;top:44px" width="126" height="8" viewBox="0 0 126 8"><line x1="0" y1="4" x2="124" y2="4" stroke="#fff" stroke-width="1"/><polyline points="120,1 124,4 120,7" fill="none" stroke="#fff" stroke-width="1"/></svg>
    <p class="about-text abs"><b>Prairie Biosolutions</b> is a distribution channel, licensed partner and manufacturers representative group providing high quality fluid handling products and technical services to the Midwestern biopharmaceutical community. With a core staff of experienced professionals and a team approach to all customer needs, we offer over 30 years of cGMP experience in the selection and use of most process consumable products. We're looking forward to working with you!</p>
    <div class="btn-navy abs">READ MORE</div>
  </section>

  <section class="products">
    <h2 class="section-title abs" style="left:81px;top:516px;color:var(--navy)">Our <span class="accent">Products</span></h2>
    <svg class="abs" style="left:81px;top:533px" width="126" height="8" viewBox="0 0 126 8"><line x1="0" y1="4" x2="124" y2="4" stroke="#27235f"/><polyline points="120,1 124,4 120,7" fill="none" stroke="#27235f"/></svg>

    <div class="slider-arrow abs" style="left:36px"><svg width="8" height="10" viewBox="0 0 8 10"><polyline points="6,1 2,5 6,9" fill="none" stroke="#fff" stroke-width="1.6"/></svg></div>
    <div class="slider-arrow abs" style="left:718px"><svg width="8" height="10" viewBox="0 0 8 10"><polyline points="2,1 6,5 2,9" fill="none" stroke="#fff" stroke-width="1.6"/></svg></div>

    <article class="card abs" style="left:81px">
      <div class="card-photo abs" role="img" aria-label="Peristaltic pump with display" style="height:178px;background:linear-gradient(#b8a8a0,#d44a2a 40%,#27235f 42%)"></div>
      <div class="card-hover abs">
        <div class="card-hover-title abs">Calder<br>Flow</div>
        <div class="card-title abs">CALDER PUMP</div>
        <p class="card-text abs">Lorem ipsum dolor sit amet, consect-etur adipisicing elit, sed do eiusmod tempor incididunt ut labore.</p>
        <span class="hover-icon abs" style="left:41px"><svg width="22" height="22" viewBox="0 0 22 22"><rect x="7.5" y="6" width="7" height="10" fill="#27235f"/><line x1="9" y1="10" x2="13" y2="10" stroke="#fff"/><line x1="9" y1="12.5" x2="13" y2="12.5" stroke="#fff"/></svg></span>
        <span class="hover-icon abs" style="left:71px"><svg width="22" height="22" viewBox="0 0 22 22"><rect x="5.5" y="9" width="7" height="4" rx="2" fill="none" stroke="#27235f" stroke-width="1.6" transform="rotate(45 9 11)"/><rect x="9.5" y="9" width="7" height="4" rx="2" fill="none" stroke="#27235f" stroke-width="1.6" transform="rotate(45 13 11)"/></svg></span>
        <div class="card-btn abs">READ MORE</div>
      </div>
    </article>

    <article class="card abs" style="left:241px">
      <div class="card-photo abs" role="img" aria-label="Liquid filling machine" style="background:linear-gradient(#f4f4f4,#cfcfcf)"></div>
      <h3 class="card-title abs" style="font-weight:400">Vexora FL20</h3>
      <p class="card-text abs">Lorem ipsum dolor sit amet, consect-etur adipisicing elit, sed do eiusmod tempor incididunt ut labore.</p>
      <div class="card-btn abs">READ MORE</div>
    </article>

    <article class="card abs" style="left:400px">
      <div class="card-photo abs" role="img" aria-label="Braided helical wire hose" style="background:linear-gradient(#2aa3d8,#7fd0ef 50%,#1b8cc4)"></div>
      <h3 class="card-title abs" style="font-weight:400">Helical wire</h3>
      <p class="card-text abs">Lorem ipsum dolor sit amet, consect-etur adipisicing elit, sed do eiusmod tempor incididunt ut labore.</p>
      <div class="card-btn abs">READ MORE</div>
    </article>

    <article class="card abs" style="left:559px">
      <div class="card-photo abs" role="img" aria-label="Modular containment cleanroom unit" style="background:linear-gradient(#e6e8ea,#bfc3c7)"></div>
      <h3 class="card-title abs" style="font-weight:400">Containment Systems</h3>
      <p class="card-text abs">Lorem ipsum dolor sit amet, consect-etur adipisicing elit, sed do eiusmod tempor incididunt ut labore.</p>
      <div class="card-btn abs">READ MORE</div>
    </article>
  </section>

  <div class="divider abs"></div>

  <section class="companies">
    <h2 class="section-title abs" style="left:81px;top:775px;color:var(--navy)">Companies <span class="accent">Represented</span></h2>
    <svg class="abs" style="left:81px;top:796px" width="126" height="8" viewBox="0 0 126 8"><line x1="0" y1="4" x2="124" y2="4" stroke="#27235f"/><polyline points="120,1 124,4 120,7" fill="none" stroke="#27235f"/></svg>
    <span class="pager abs" style="left:667px;background:var(--navy)"><svg width="9" height="8" viewBox="0 0 9 8"><polyline points="4,1 1,4 4,7" fill="none" stroke="#fff"/><polyline points="8,1 5,4 8,7" fill="none" stroke="#fff"/></svg></span>
    <span class="pager abs" style="left:686px;background:var(--orange)"><svg width="9" height="8" viewBox="0 0 9 8"><polyline points="1,1 4,4 1,7" fill="none" stroke="#fff"/><polyline points="5,1 8,4 5,7" fill="none" stroke="#fff"/></svg></span>
    <div class="partner abs" style="left:81px">Cleanvale</div>
    <div class="partner abs" style="left:187px">Calder Flow</div>
    <div class="partner abs" style="left:294px">Vexora</div>
    <div class="partner abs" style="left:399px">Norland Polymers</div>
    <div class="partner abs" style="left:506px">Aptiva</div>
    <div class="partner abs" style="left:612px">Modulair</div>
  </section>

  <footer class="footer abs">
    <div class="brand abs"><span class="brand-dot"></span>Prairie Bio</div>
    <p class="footer-text abs">Lorem Ipsum has been the industry's standard dummy text ever since the 1500s When an unknown printer took.</p>
    <span class="big-social abs primary" style="left:81px"></span>
    <span class="big-social abs" style="left:116px"></span>
    <span class="big-social abs" style="left:150px"></span>
    <span class="big-social abs" style="left:185px"></span>

    <div class="person-photo abs" style="left:262px;background:linear-gradient(#8ab0c8,#d9b89c)" role="img" aria-label="Portrait of K. Reyes"></div>
    <svg class="abs" style="left:310px;top:143px" width="11" height="11" viewBox="0 0 11 11"><rect width="11" height="11" rx="2" fill="#111"/><path d="M3 2.5l1.5 0 .6 1.8-.9.7a5 5 0 0 0 2 2l.7-.9 1.8.6 0 1.5c-3.5 0-5.7-2.2-5.7-5.7z" fill="#fff"/></svg>
    <p class="contact-line abs" style="left:240px;top:159px">(555) 214-3380</p>
    <svg class="abs" style="left:310px;top:183px" width="12" height="9" viewBox="0 0 12 9"><rect width="12" height="9" fill="#111"/><polyline points="0,0 6,5 12,0" fill="none" stroke="#fff"/></svg>
    <p class="contact-line abs" style="left:240px;top:198px">kreyes@prairie-bio.com</p>
    <span class="mini-social abs primary" style="left:270px"></span>
    <span class="mini-social abs" style="left:292px"></span>
    <span class="mini-social abs" style="left:314px"></span>
    <span class="mini-social abs" style="left:335px"></span>

    <div class="person-photo abs" style="left:419px;background:linear-gradient(#6d6a7e,#8a6f66)" role="img" aria-label="Portrait of Dan Whitmore"></div>
    <svg class="abs" style="left:466px;top:143px" width="11" height="11" viewBox="0 0 11 11"><rect width="11" height="11" rx="2" fill="#111"/><path d="M3 2.5l1.5 0 .6 1.8-.9.7a5 5 0 0 0 2 2l.7-.9 1.8.6 0 1.5c-3.5 0-5.7-2.2-5.7-5.7z" fill="#fff"/></svg>
    <p class="contact-line abs" style="left:397px;top:159px">(555) 407-9126</p>
    <svg class="abs" style="left:466px;top:183px" width="12" height="9" viewBox="0 0 12 9"><rect width="12" height="9" fill="#111"/><polyline points="0,0 6,5 12,0" fill="none" stroke="#fff"/></svg>
    <p class="contact-line abs" style="left:387px;top:198px;width:170px">dwhitmore@prairie-bio.com</p>
    <span class="mini-social abs primary" style="left:431px"></span>
    <span class="mini-social abs" style="left:452px"></span>
    <span class="mini-social abs" style="left:474px"></span>
    <span class="mini-social abs" style="left:495px"></span>

    <div class="field abs" style="top:30px;height:24px">Name :</div>
    <div class="field abs" style="top:61px;height:24px">Email :</div>
    <div class="field abs" style="top:91px;height:98px">Message :</div>
    <div class="btn-send abs">SEND</div>
  </footer>

  <div class="copyright abs">© Prairie Biosolutions, Corp.</div>
</div>
</body>
</html>
```